Design a web site for my business - Brellan Coatworks Mackaby.

We are a family business that handles design, fabrication and installation of powder coated aluminum, stainless steel and glass products. Including handrails, privacy slat screens, electric gates and pool fencing. We are based in the Whitsundays in North Queensland and service an area from Airlie Beach to Townsville.

Target Market(s)

Domestic and commercial

Industry/Entity Type

fabrication - manufacturing

Coding

Coded - Design and coding required

Number of Pages Required

5+ page

Colors
0054AA
0677BA
7BADD7
CADEEF
E8F1F8

Requirements
Must have
• photo galleries, contact page, one page for privacy screens, balustrades, glass fencing, stainless steel handrail, powder coated aluminium handrails and pool fencing

```html
<!DOCTYPE html>
<html lang="en">
<head>
<meta charset="utf-8">
<title>Brellan Coatworks Mackaby — Design, Fabrication, Installation</title>
<link rel="stylesheet" href="https://fonts.googleapis.com/css2?family=Barlow+Condensed:wght@600;700&family=Barlow:wght@400;500;600;700&display=swap">
<style>
:root{
  --blue-deep:#0054AA;
  --blue:#0677BA;
  --blue-mid:#7BADD7;
  --blue-soft:#CADEEF;
  --blue-pale:#E8F1F8;
  --navy:#0E1F3B;
  --navy-card:#17294a;
  --ink:#0f1d33;
  --text:#4a5566;
  --white:#ffffff;
  --line:#dfe6ee;
}
*{box-sizing:border-box;margin:0;padding:0}
html,body{width:1200px;height:4249px;overflow:hidden}
body{font-family:"Barlow",Arial,sans-serif;color:var(--ink);background:var(--white);font-size:12px;line-height:1.6}
.wrap{width:840px;margin:0 auto;position:relative}
h1,h2,h3,h4,.cond{font-family:"Barlow Condensed","Arial Narrow",sans-serif;text-transform:uppercase;font-weight:700;letter-spacing:.2px}
a{color:inherit;text-decoration:none}
.eyebrow{display:flex;align-items:center;gap:10px;font-size:10px;font-weight:600;letter-spacing:3px;text-transform:uppercase;color:var(--blue)}
.eyebrow::before{content:"";width:28px;height:1.5px;background:currentColor}
.eyebrow.center{justify-content:center}
.eyebrow.center::before{display:none}

/* top bar */
.topbar{height:22px;background:var(--blue-deep);color:var(--white);font-size:9.5px}
.topbar .wrap{display:flex;align-items:center;height:22px}
.topbar .sep{margin:0 18px;opacity:.6}
.topbar .call{margin-left:auto;font-weight:700;letter-spacing:.5px}

/* nav */
.nav{height:62px;background:var(--white);border-bottom:1px solid var(--line)}
.nav .wrap{display:flex;align-items:center;height:62px}
.brand{display:flex;align-items:center;gap:8px;font-weight:700;font-size:11px;color:var(--navy)}
.brand .mark{width:14px;height:14px;border-radius:50%;background:var(--blue)}
.menu{margin-left:auto;display:flex;gap:22px;font-size:11px;font-weight:600;align-items:center}
.menu .active{color:var(--blue)}
.btn{display:inline-block;font-size:10.5px;font-weight:700;letter-spacing:1px;text-transform:uppercase;padding:0 22px;line-height:35px;border-radius:2px}
.btn-primary{background:var(--blue);color:var(--white)}
.btn-outline{border:1.5px solid var(--white);color:var(--white);line-height:32px}
.menu .btn{line-height:28px;padding:0 16px;font-size:10px}

/* hero */
.hero{height:458px;position:relative;background:linear-gradient(100deg,#1c2e46 0%,#2f4a68 35%,#5d86ad 65%,#8db4d6 100%);color:var(--white)}
.hero .photo{position:absolute;inset:0}
.hero .wrap{padding-top:100px}
.hero .eyebrow{color:var(--blue-soft)}
.hero h1{font-size:46px;line-height:1.02;margin-top:18px}
.hero p{font-size:12.5px;width:380px;margin-top:18px;line-height:1.75;color:#e6eef7}
.hero .actions{display:flex;gap:12px;margin-top:22px}

/* features */
.features{height:89px;background:var(--blue-deep);color:var(--white)}
.features .wrap{display:grid;grid-template-columns:repeat(4,1fr);gap:14px;padding-top:20px}
.feature{border-left:1.5px solid rgba(255,255,255,.5);padding-left:12px}
.feature h4{font-size:14px;line-height:1.2}
.feature p{font-size:9.5px;line-height:1.55;color:#d3e2f2;margin-top:3px;width:170px}

/* about */
.about{height:439px}
.about .wrap{display:flex;padding-top:62px}
.about .copy{width:390px;padding-top:26px}
.about h2{font-size:30px;line-height:1.08;margin-top:12px}
.about p{font-size:11.5px;color:var(--text);margin-top:14px;line-height:1.8}
.link{display:inline-block;font-size:10px;font-weight:700;letter-spacing:1px;text-transform:uppercase;color:var(--blue-deep);border-bottom:1.5px solid var(--blue-deep);margin-top:16px;padding-bottom:1px}
.about .figure{position:absolute;left:446px;top:62px;width:394px;height:314px}
.ph{display:block;width:100%;height:100%}
.badge{position:absolute;left:-14px;bottom:-13px;width:210px;height:64px;background:var(--blue);color:var(--white);padding:12px 18px;border-radius:2px;box-shadow:0 8px 18px rgba(0,40,90,.25)}
.badge strong{font-family:"Barlow Condensed",sans-serif;font-size:22px;line-height:1}
.badge span{display:block;font-size:9px;margin-top:2px}

/* products */
.products{height:1110px;background:var(--blue-pale)}
.products .wrap{padding-top:64px}
.section-head{display:flex;justify-content:space-between;align-items:flex-end}
.section-head h2{font-size:30px;line-height:1;margin-top:12px}
.section-head .intro{width:300px;font-size:11px;color:var(--text);line-height:1.7}
.grid-products{display:grid;grid-template-columns:repeat(3,268px);gap:20px 18px;margin-top:32px}
.card{background:var(--white);border-radius:3px;overflow:hidden;height:298px;box-shadow:0 1px 3px rgba(15,30,60,.06)}
.card.short{height:278px}
.card .img{height:163px}
.card .body{padding:16px 17px}
.card h3{font-size:15.5px;line-height:1.25}
.card p{font-size:10px;color:var(--text);margin-top:6px;line-height:1.65}
.card .more{display:block;font-size:9.5px;font-weight:700;letter-spacing:1px;color:var(--blue-deep);margin-top:8px}

/* process */
.process{height:396px;background:var(--navy);color:var(--white)}
.process .wrap{padding-top:64px;text-align:center}
.process .eyebrow{color:var(--blue-mid)}
.process h2{font-size:30px;margin-top:8px}
.steps{display:grid;grid-template-columns:repeat(3,268px);gap:18px;margin-top:26px;text-align:left}
.step{background:var(--navy-card);border:1px solid #2a3d5e;border-radius:3px;height:179px;padding:24px 22px}
.step .num{font-family:"Barlow Condensed",sans-serif;font-weight:700;font-size:32px;color:var(--blue);line-height:1}
.step h3{font-size:17px;margin-top:12px}
.step p{font-size:10px;color:#aab6c8;line-height:1.8;margin-top:6px}

/* gallery */
.gallery{height:536px}
.gallery .wrap{padding-top:64px}
.grid-gallery{display:grid;grid-template-columns:414px 202px 202px;grid-template-rows:157px 157px;gap:10px 11px;margin-top:30px}
.tile{position:relative;border-radius:2px;overflow:hidden}
.tile.big{grid-row:span 2}
.tag{position:absolute;left:10px;bottom:10px;background:rgba(14,31,59,.82);color:var(--white);font-size:9.5px;padding:3px 8px;border-radius:2px}

/* service area */
.area{height:413px;background:var(--blue-pale)}
.area .wrap{display:flex;align-items:center;height:413px}
.area .copy{width:400px}
.area h2{font-size:30px;margin-top:12px;line-height:1}
.area p{font-size:11.5px;color:var(--text);margin-top:14px;line-height:1.75}
.chips{display:flex;flex-wrap:wrap;gap:8px 7px;margin-top:14px;width:390px}
.chip{background:var(--white);border:1px solid var(--blue-soft);border-radius:20px;font-size:9.5px;font-weight:500;padding:3px 12px}
.area .map{position:absolute;right:0;top:56px;width:398px;height:301px;border-radius:3px;overflow:hidden;border:1px solid var(--blue-soft)}

/* quote */
.quote{height:459px;background:linear-gradient(135deg,var(--blue-deep),var(--blue));color:var(--white)}
.quote .wrap{display:flex;align-items:center;height:459px}
.quote .copy{width:400px;padding-top:10px}
.quote h2{font-size:32px;line-height:1}
.quote p{font-size:12px;margin-top:12px;line-height:1.75;color:#e3eefa}
.contact-list{list-style:none;margin-top:14px}
.contact-list li{font-size:11.5px;display:flex;align-items:center;gap:10px;margin-top:6px}
.contact-list li::before{content:"";width:5px;height:5px;border-radius:50%;background:var(--white)}
.form{position:absolute;right:0;top:64px;width:358px;height:332px;background:var(--white);color:var(--ink);border-radius:4px;padding:28px 26px}
.form h3{font-size:17px}
.field{display:block;width:100%;height:32px;border:1px solid #d3dbe5;border-radius:2px;margin-top:11px;font-size:9.5px;color:#7a8595;padding:0 10px;line-height:30px;position:relative;background:var(--white)}
.field.area-field{height:70px}
.field.select::after{content:"";position:absolute;right:10px;top:12px;width:5px;height:5px;border-right:1px solid #555;border-bottom:1px solid #555;transform:rotate(45deg)}
.submit{display:block;width:100%;height:34px;background:var(--blue);color:var(--white);text-align:center;line-height:34px;font-size:10.5px;font-weight:700;letter-spacing:1.2px;margin-top:12px;border-radius:2px}

/* footer */
.footer{height:265px;background:var(--navy);color:#aeb9c9}
.footer .wrap{display:grid;grid-template-columns:352px 260px 228px;padding-top:44px}
.footer .brand{color:var(--white)}
.footer .about-text{font-size:9.5px;line-height:1.75;width:240px;margin-top:18px}
.footer h4{font-size:12px;color:var(--white);letter-spacing:1.5px}
.footer ul{list-style:none;margin-top:6px}
.footer li{font-size:9.5px;line-height:2.1}
.legal{position:absolute;left:0;right:0;top:224px;display:flex;justify-content:space-between;font-size:8.5px;color:#8290a6}
.footer-line{position:absolute;left:0;right:0;top:210px;height:1px;background:#26385a}
</style>
</head>
<body>

<div class="topbar">
  <div class="wrap">
    <span>Servicing Airlie Beach to Townsville</span><span class="sep">|</span><span>Family owned &amp; operated in the Whitsundays</span>
    <span class="call">CALL (07) 4700 1234</span>
  </div>
</div>

<header class="nav">
  <div class="wrap">
    <a class="brand" href="#"><span class="mark"></span>Brellan Coatworks Mackaby</a>
    <nav class="menu">
      <a class="active" href="#">Home</a>
      <a href="#">Products</a>
      <a href="#">Gallery</a>
      <a href="#">Service Area</a>
      <a class="btn btn-primary" href="#">Get a quote</a>
    </nav>
  </div>
</header>

<section class="hero">
  <svg class="photo" role="img" aria-label="Harbour foreshore with rock wall, palms and a boardwalk handrail at dusk" viewBox="0 0 1200 458" preserveAspectRatio="none">
    <defs>
      <linearGradient id="heroShade" x1="0" x2="1">
        <stop offset="0" stop-color="#0e1f3b" stop-opacity=".75"/>
        <stop offset=".55" stop-color="#0e1f3b" stop-opacity=".25"/>
        <stop offset="1" stop-color="#0e1f3b" stop-opacity="0"/>
      </linearGradient>
    </defs>
    <rect width="1200" height="458" fill="url(#heroShade)"/>
  </svg>
  <div class="wrap">
    <div class="eyebrow">Design · Fabrication · Installation</div>
    <h1>Built for the tropics.<br>Finished to last.</h1>
    <p>Powder coated aluminium, stainless steel and glass — handrails, balustrades, privacy screens, pool fencing and electric gates, custom fabricated in the Whitsundays.</p>
    <div class="actions">
      <a class="btn btn-primary" href="#">Request a quote</a>
      <a class="btn btn-outline" href="#">Our products</a>
    </div>
  </div>
</section>

<section class="features">
  <div class="wrap">
    <div class="feature"><h4>Family owned</h4><p>Local Whitsundays business, one team start to finish</p></div>
    <div class="feature"><h4>Marine grade</h4><p>316 stainless &amp; powder coated aluminium for coastal life</p></div>
    <div class="feature"><h4>Fully compliant</h4><p>Built to Australian Standards, QBCC licensed</p></div>
    <div class="feature"><h4>Wide service area</h4><p>Airlie Beach to Townsville, islands included</p></div>
  </div>
</section>

<section class="about">
  <div class="wrap">
    <div class="copy">
      <div class="eyebrow">Family owned &amp; operated</div>
      <h2>One team, from first sketch to final install</h2>
      <p>We're a Whitsundays family business handling the whole job in-house — measure and design, fabrication in our workshop, powder coating, and installation on site. No middlemen, no handballing. Marine-grade materials chosen for North Queensland's salt, sun and cyclone conditions.</p>
      <p>From a single pool fence to full commercial foreshore projects, we work with homeowners, builders and councils from Airlie Beach to Townsville.</p>
      <a class="link" href="#">Talk to us about your project →</a>
    </div>
    <div class="figure">
      <svg class="ph" role="img" aria-label="Timber boardwalk stairs with stainless steel handrails among rocks and bush" viewBox="0 0 10 10" preserveAspectRatio="none">
        <defs><linearGradient id="g1" x1="0" y1="0" x2="1" y2="1"><stop offset="0" stop-color="#3f5a3c"/><stop offset=".55" stop-color="#8a7a68"/><stop offset="1" stop-color="#6f7c6a"/></linearGradient></defs>
        <rect width="10" height="10" fill="url(#g1)"/>
      </svg>
      <div class="badge"><strong>100%</strong><span>designed, fabricated &amp; installed by us</span></div>
    </div>
  </div>
</section>

<section class="products">
  <div class="wrap">
    <div class="section-head">
      <div>
        <div class="eyebrow">What we build</div>
        <h2>Products &amp; services</h2>
      </div>
      <p class="intro">Every product is custom measured, fabricated to Australian Standards and powder coated in your choice of colour.</p>
    </div>
    <div class="grid-products">
      <article class="card">
        <svg class="ph img" role="img" aria-label="Bronze powder coated handrail along a waterfront path" viewBox="0 0 10 10" preserveAspectRatio="none"><defs><linearGradient id="p1" x1="0" y1="0" x2="0" y2="1"><stop offset="0" stop-color="#8fb2d4"/><stop offset=".5" stop-color="#5b7390"/><stop offset="1" stop-color="#8a5a34"/></linearGradient></defs><rect width="10" height="10" fill="url(#p1)"/></svg>
        <div class="body"><h3>Powder coated aluminium handrails</h3><p>Durable, low-maintenance handrails in any powder coat colour — built for coastal conditions.</p><a class="more" href="#">LEARN MORE →</a></div>
      </article>
      <article class="card">
        <svg class="ph img" role="img" aria-label="Stainless steel handrails on timber stairs" viewBox="0 0 10 10" preserveAspectRatio="none"><defs><linearGradient id="p2" x1="0" y1="0" x2="1" y2="1"><stop offset="0" stop-color="#3f5a3c"/><stop offset="1" stop-color="#8a7a68"/></linearGradient></defs><rect width="10" height="10" fill="url(#p2)"/></svg>
        <div class="body"><h3>Stainless steel handrails</h3><p>Marine-grade 316 stainless handrails and wire balustrades, polished or brushed finish.</p><a class="more" href="#">LEARN MORE →</a></div>
      </article>
      <article class="card">
        <svg class="ph img" role="img" aria-label="Glass balustrade on an elevated timber deck" viewBox="0 0 10 10" preserveAspectRatio="none"><defs><linearGradient id="p3" x1="0" y1="0" x2="0" y2="1"><stop offset="0" stop-color="#3a2e28"/><stop offset=".6" stop-color="#7d7f82"/><stop offset="1" stop-color="#b4bcc2"/></linearGradient></defs><rect width="10" height="10" fill="url(#p3)"/></svg>
        <div class="body"><h3>Balustrades</h3><p>Glass, stainless and aluminium balustrades for decks, stairs and balconies — compliant to AS1170.</p><a class="more" href="#">LEARN MORE →</a></div>
      </article>
      <article class="card short">
        <svg class="ph img" role="img" aria-label="Frameless glass fence beside a paved garden" viewBox="0 0 10 10" preserveAspectRatio="none"><defs><linearGradient id="p4" x1="0" y1="0" x2="1" y2="1"><stop offset="0" stop-color="#2f4a30"/><stop offset="1" stop-color="#a9aeac"/></linearGradient></defs><rect width="10" height="10" fill="url(#p4)"/></svg>
        <div class="body"><h3>Glass fencing</h3><p>Frameless and semi-frameless glass fencing that keeps your view exactly where it should be.</p><a class="more" href="#">LEARN MORE →</a></div>
      </article>
      <article class="card short">
        <svg class="ph img" role="img" aria-label="Cream aluminium slat privacy screen and gates" viewBox="0 0 10 10" preserveAspectRatio="none"><defs><linearGradient id="p5" x1="0" y1="0" x2="0" y2="1"><stop offset="0" stop-color="#2c5db0"/><stop offset=".45" stop-color="#d8d2c0"/><stop offset="1" stop-color="#9a968c"/></linearGradient></defs><rect width="10" height="10" fill="url(#p5)"/></svg>
        <div class="body"><h3>Privacy slat screens</h3><p>Custom aluminium slat screens and gates for privacy, pool equipment, bins and courtyards.</p><a class="more" href="#">LEARN MORE →</a></div>
      </article>
      <article class="card short">
        <svg class="ph img" role="img" aria-label="Glass pool fence with tropical plants" viewBox="0 0 10 10" preserveAspectRatio="none"><defs><linearGradient id="p6" x1="1" y1="0" x2="0" y2="1"><stop offset="0" stop-color="#2f4a30"/><stop offset="1" stop-color="#a9aeac"/></linearGradient></defs><rect width="10" height="10" fill="url(#p6)"/></svg>
        <div class="body"><h3>Pool fencing</h3><p>Compliant aluminium and glass pool fencing, certified to QLD pool safety standards.</p><a class="more" href="#">LEARN MORE →</a></div>
      </article>
      <article class="card short">
        <svg class="ph img" role="img" aria-label="Aluminium slat electric gate" viewBox="0 0 10 10" preserveAspectRatio="none"><defs><linearGradient id="p7" x1="0" y1="0" x2="0" y2="1"><stop offset="0" stop-color="#2c5db0"/><stop offset=".45" stop-color="#d8d2c0"/><stop offset="1" stop-color="#9a968c"/></linearGradient></defs><rect width="10" height="10" fill="url(#p7)"/></svg>
        <div class="body"><h3>Electric gates</h3><p>Automated sliding and swing gates with remote and keypad access, fabricated to suit your entry.</p><a class="more" href="#">LEARN MORE →</a></div>
      </article>
    </div>
  </div>
</section>

<section class="process">
  <div class="wrap">
    <div class="eyebrow center">How we work</div>
    <h2>Design. Fabricate. Install.</h2>
    <div class="steps">
      <div class="step"><div class="num">01</div><h3>Design &amp; measure</h3><p>We visit your site, measure up and design the job with you — materials, finish and powder coat colour.</p></div>
      <div class="step"><div class="num">02</div><h3>Fabricate &amp; coat</h3><p>Everything is fabricated in our Whitsundays workshop and powder coated for a finish that survives salt and sun.</p></div>
      <div class="step"><div class="num">03</div><h3>Install</h3><p>Our own installers fit the job on site, on schedule — and leave it certified, clean and ready to use.</p></div>
    </div>
  </div>
</section>

<section class="gallery">
  <div class="wrap">
    <div class="section-head">
      <div>
        <div class="eyebrow">Recent projects</div>
        <h2>From the gallery</h2>
      </div>
      <a class="link" href="#" style="margin-bottom:4px">View full gallery →</a>
    </div>
    <div class="grid-gallery">
      <div class="tile big">
        <svg class="ph" role="img" aria-label="Foreshore handrails at Airlie Beach with flame trees and water" viewBox="0 0 10 10" preserveAspectRatio="none"><defs><linearGradient id="q1" x1="0" y1="0" x2="0" y2="1"><stop offset="0" stop-color="#90b3d5"/><stop offset=".5" stop-color="#55708c"/><stop offset="1" stop-color="#8a5a34"/></linearGradient></defs><rect width="10" height="10" fill="url(#q1)"/></svg>
        <span class="tag">Foreshore handrails · Airlie Beach</span>
      </div>
      <div class="tile">
        <svg class="ph" role="img" aria-label="Frameless glass fence in a garden" viewBox="0 0 10 10" preserveAspectRatio="none"><defs><linearGradient id="q2" x1="0" y1="0" x2="1" y2="1"><stop offset="0" stop-color="#2f4a30"/><stop offset="1" stop-color="#a9aeac"/></linearGradient></defs><rect width="10" height="10" fill="url(#q2)"/></svg>
        <span class="tag">Frameless glass</span>
      </div>
      <div class="tile">
        <svg class="ph" role="img" aria-label="Aluminium slat screens" viewBox="0 0 10 10" preserveAspectRatio="none"><defs><linearGradient id="q3" x1="0" y1="0" x2="0" y2="1"><stop offset="0" stop-color="#2c5db0"/><stop offset=".45" stop-color="#d8d2c0"/><stop offset="1" stop-color="#9a968c"/></linearGradient></defs><rect width="10" height="10" fill="url(#q3)"/></svg>
        <span class="tag">Slat screens</span>
      </div>
      <div class="tile">
        <svg class="ph" role="img" aria-label="Glass balustrade on a deck" viewBox="0 0 10 10" preserveAspectRatio="none"><defs><linearGradient id="q4" x1="0" y1="0" x2="0" y2="1"><stop offset="0" stop-color="#3a2e28"/><stop offset=".6" stop-color="#7d7f82"/><stop offset="1" stop-color="#b4bcc2"/></linearGradient></defs><rect width="10" height="10" fill="url(#q4)"/></svg>
        <span class="tag">Balustrades</span>
      </div>
      <div class="tile">
        <svg class="ph" role="img" aria-label="Stainless handrails on boardwalk stairs" viewBox="0 0 10 10" preserveAspectRatio="none"><defs><linearGradient id="q5" x1="0" y1="0" x2="1" y2="1"><stop offset="0" stop-color="#3f5a3c"/><stop offset="1" stop-color="#8a7a68"/></linearGradient></defs><rect width="10" height="10" fill="url(#q5)"/></svg>
        <span class="tag">Stainless handrails</span>
      </div>
    </div>
  </div>
</section>

<section class="area">
  <div class="wrap">
    <div class="copy">
      <div class="eyebrow">Where we work</div>
      <h2>Airlie Beach to Townsville</h2>
      <p>Based in the Whitsundays, we service residential and commercial projects across the North Queensland coast — including the islands.</p>
      <div class="chips">
        <span class="chip">Airlie Beach</span><span class="chip">Cannonvale</span><span class="chip">Proserpine</span><span class="chip">Bowen</span><span class="chip">Ayr</span><span class="chip">Townsville</span><span class="chip">Whitsunday Islands</span>
      </div>
    </div>
    <div class="map">
      <svg class="ph" role="img" aria-label="Map of the North Queensland coast from Townsville to Airlie Beach" viewBox="0 0 10 10" preserveAspectRatio="none"><defs><linearGradient id="m1" x1="0" y1="0" x2="1" y2="0"><stop offset="0" stop-color="#cfe6d2"/><stop offset=".5" stop-color="#bfe3cc"/><stop offset=".65" stop-color="#8fd8ea"/><stop offset="1" stop-color="#7dd2e8"/></linearGradient></defs><rect width="10" height="10" fill="url(#m1)"/></svg>
    </div>
  </div>
</section>

<section class="quote">
  <div class="wrap">
    <div class="copy">
      <h2>Get a free measure &amp; quote</h2>
      <p>Tell us about your project and we'll come to you. Most quotes turned around within a week.</p>
      <ul class="contact-list">
        <li>(07) 4700 1234</li>
        <li>quotes@brellancoatworks.com.au</li>
        <li>Whitsundays, North Queensland</li>
      </ul>
    </div>
    <form class="form">
      <h3>Request a quote</h3>
      <span class="field">Your name</span>
      <span class="field">Phone</span>
      <span class="field select" style="color:var(--ink)">Powder coated aluminium handrails</span>
      <span class="field area-field">Tell us about the project ...</span>
      <span class="submit">SEND REQUEST</span>
    </form>
  </div>
</section>

<footer class="footer">
  <div class="wrap">
    <div>
      <a class="brand" href="#"><span class="mark"></span>Brellan Coatworks Mackaby</a>
      <p class="about-text">Family owned design, fabrication and installation of powder coated aluminium, stainless steel and glass products in North Queensland.</p>
    </div>
    <div>
      <h4>Products</h4>
      <ul><li>Powder coated handrails</li><li>Stainless steel handrails</li><li>Balustrades</li><li>Glass fencing</li><li>Privacy screens</li><li>Pool fencing</li><li>Electric gates</li></ul>
    </div>
    <div>
      <h4>Contact</h4>
      <ul><li>(07) 4700 1234</li><li>quotes@brellancoatworks.com.au</li><li>Whitsundays QLD</li><li>Mon–Fri 7am – 4pm</li></ul>
    </div>
    <div class="footer-line"></div>
    <div class="legal"><span>© 2026 Brellan Coatworks Mackaby. All rights reserved.</span><span>QBCC Licensed · Fully Insured</span></div>
  </div>
</footer>

</body>
</html>
```